Update our business cards to match our awesome new website

Need a new design for company business cards. We have recently revamped our website and would like our business cards to get a refresh too. I've uploaded the company artwork, logo, as well as the Branding Deck to better understand the look & feel of our brand. Please visit the website at hollowbrookestatesmi.com.

Industry/Entity Type

Real Estate

Contact Information for Business Card

must use the colors outlined in the Branding Deck uploaded to the site, or the colors of our logo.

Font styles to use
Other font styles liked:
• Calibri

Requirements
Must have
• Required items: Name, title, company logo, address: 218 Fenwick St. Suite 300, Northville, MI 48173, email address: cole@hollowbrookestatesMI.com, company phone 800-555-0193, cell: 248-555-0162
Nice to have
• a more simple design. not complicated
Should not have
• cartoonish characters, or whimsical writing or artwork, stay within our branding colors

```html
<!DOCTYPE html>
<html lang="en">
<head>
<meta charset="utf-8">
<title>Hollowbrook Estates – Business Cards</title>
<link href="https://fonts.googleapis.com/css2?family=Carlito:wght@400;700&display=swap" rel="stylesheet">
<style>
  :root {
    --page-bg: #f2f2f2;
    --card-white: #ffffff;
    --card-black: #231f20;
    --ink: #231f20;
    --icon-blue: #1a6bc4;
    --card-border: #3a3a3a;
    --leaf-light: #c9dfa6;
    --leaf-mid: #9dbf82;
    --sun-orange: #f6a26c;
  }
  * { box-sizing: border-box; margin: 0; padding: 0; }
  html, body {
    width: 1200px; height: 675px; overflow: hidden;
    background: var(--page-bg);
    font-family: "Carlito", "Calibri", Arial, sans-serif;
    color: var(--ink);
  }
  .sheet {
    width: 1200px; height: 675px;
    display: flex; align-items: center; justify-content: center; gap: 40px;
  }
  .card {
    position: relative;
    width: 540px; height: 308px;
    overflow: hidden;
  }
  .card--front { background: var(--card-white); border: 1px solid var(--card-border); }
  .card--back { background: var(--card-black); }

  .brand-name { font-weight: 400; letter-spacing: 0.5px; white-space: nowrap; }
  .card--front .brand-name {
    position: absolute; right: 34px; top: 74px;
    font-size: 21px; color: var(--ink);
  }
  .card--back .brand-name {
    position: absolute; left: 0; right: 0; top: 160px; text-align: center;
    font-size: 36px; color: var(--card-white);
  }

  .person { position: absolute; left: 32px; top: 88px; }
  .person__name { font-size: 22px; line-height: 1; }
  .person__title { font-size: 14.5px; margin-top: 4px; letter-spacing: 0.3px; }

  .contact { position: absolute; left: 28px; top: 150px; list-style: none; font-size: 14.5px; line-height: 18px; }
  .contact__item { display: flex; align-items: flex-start; gap: 8px; }
  .contact__item + .contact__item { margin-top: 2px; }
  .contact__item--gap { margin-top: 9px !important; }
  .contact__icon { width: 16px; height: 16px; flex: none; margin-top: 1px; fill: var(--icon-blue); }

  .tree-art {
    position: absolute; left: 330px; top: 130px; width: 170px; height: 178px;
    background: radial-gradient(ellipse at 40% 45%, var(--leaf-mid) 0%, var(--leaf-light) 55%, rgba(246,162,108,0.35) 80%, rgba(255,255,255,0) 100%);
  }
</style>
</head>
<body>
<main class="sheet">
  <section class="card card--front" aria-label="Business card front">
    <p class="brand-name">Hollowbrook Estates</p>
    <div class="person">
      <p class="person__name">Cole Ashworth</p>
      <p class="person__title">MANAGING DIRECTOR</p>
    </div>
    <ul class="contact">
      <li class="contact__item">
        <svg class="contact__icon" viewBox="0 0 16 16"><path d="M8 1a5 5 0 0 0-5 5c0 3.6 5 9 5 9s5-5.4 5-9a5 5 0 0 0-5-5zm0 7a2 2 0 1 1 0-4 2 2 0 0 1 0 4z"/></svg>
        <span>218 Fenwick St. Suite<br>300, Northville, MI 48173</span>
      </li>
      <li class="contact__item contact__item--gap">
        <svg class="contact__icon" viewBox="0 0 16 16"><path d="M1 6c0-2 3-3.5 7-3.5S15 4 15 6v1.5h-3.5V6h-7v1.5H1z"/><path d="M4 8h8l2 5H2z"/><circle cx="8" cy="10.5" r="1.5" fill="#fff"/></svg>
        <span>800-555-0193</span>
      </li>
      <li class="contact__item">
        <svg class="contact__icon" viewBox="0 0 16 16"><path d="M5 1h6a1 1 0 0 1 1 1v12a1 1 0 0 1-1 1H5a1 1 0 0 1-1-1V2a1 1 0 0 1 1-1zm.5 1.8v9.4h5V2.8z"/></svg>
        <span>248-555-0162</span>
      </li>
      <li class="contact__item contact__item--gap">
        <svg class="contact__icon" viewBox="0 0 16 16"><path d="M1 3.5h14v9H1z"/><path d="M1.5 4l6.5 5 6.5-5" fill="none" stroke="#fff" stroke-width="1.3"/></svg>
        <span>cole@hollowbrookestatesMI.com</span>
      </li>
      <li class="contact__item">
        <svg class="contact__icon" viewBox="0 0 16 16" fill="none" stroke="#1a6bc4" stroke-width="1.2" style="fill:none"><circle cx="8" cy="8" r="6.5"/><ellipse cx="8" cy="8" rx="3" ry="6.5"/><path d="M1.5 8h13M2.5 4.8h11M2.5 11.2h11"/></svg>
        <span>www.hollowbrookestatesmi.com</span>
      </li>
    </ul>
    <div class="tree-art" role="img" aria-label="Soft illustration of a green tree with an orange sun behind it"></div>
  </section>

  <section class="card card--back" aria-label="Business card back">
    <p class="brand-name">Hollowbrook Estates</p>
  </section>
</main>
</body>
</html>
```